Visitenkarten-Design für Hotel und Restaurant in der Fußgängerzone
Zielgruppe
Hotel und Restaurant in der Fußgängerzone, zwei Gehminuten zum Bodensee.
Neu renoviertes Hotel/Restaurant (z.B.Boxspringbett, Holzboden, USB Steckdosen).
Übernachtung mit Frühstück im Einzel,-Doppel,- oder Komfortzimmer (für 3 Personen).
Restaurant mit regionaler Küche. Besondere saisonale Zutaten unserer Nachbarländer als Specials.
Touristen im Sommer Durchschnittalter: 50 Jahre, sportlich, modern, gut betucht.
Einwohner der Stadt im Winter, Alter zwischen 25 und 65 Jahre, viele davon Hausbesitzer, Segelboot Besitzer etc.
Aufgabenstellung
Farbkonzept im Restaurant:
warm- weiße Wände, dunkle Holzmöbel, rote Barelemente, weiß-kupferfarbene Lampen.
Würden uns etwas minimalistisches wünschen, trotzdem mit einem Wow Effekt.
Sei es ein ausgeschnittenes Logo, abgerundete Ecken, besonderes Material usw.
Dateianhänge sind nur für´s bessere Verständnis, muss nicht zwingend als Vorgabe gesehen werden.
Vorderseite:
Logo
Hotel & Restaurant (kann, muss aber nicht draufstehen.)
zum Anker
Seestadt

```html
<!DOCTYPE html>
<html lang="de">
<head>
<meta charset="utf-8">
<title>zum Anker – Visitenkarte</title>
<link href="https://fonts.googleapis.com/css2?family=Open+Sans:wght@400;600&display=swap" rel="stylesheet">
<style>
  :root {
    --page: #ffffff;
    --ink: #111111;
    --card-dark: #050505;
    --pattern-tone: #1c1c1c;
    --card-light: #ffffff;
    --card-edge: #3a3a3a;
    --band: #808285;
    --band-light: #9a9b9d;
    --paper: #ffffff;
  }
  * { box-sizing: border-box; margin: 0; padding: 0; }
  html, body {
    width: 994px; height: 1200px; overflow: hidden;
    background: var(--page);
    font-family: "Open Sans", Arial, sans-serif;
  }
  .canvas { position: relative; width: 994px; height: 1200px; }

  .card {
    position: absolute; left: 78px; width: 835px; height: 508px;
    border-radius: 28px; overflow: hidden;
  }
  .card--front { top: 90px; background: var(--card-dark); }
  .card--back { top: 620px; background: var(--card-light); border: 1px solid var(--card-edge); }

  .front-pattern {
    position: absolute; inset: 0;
    background: radial-gradient(circle at 50% 50%, var(--pattern-tone), var(--card-dark) 80%);
  }

  .brand { position: absolute; width: 320px; text-align: center; }
  .brand__dot {
    position: absolute; left: 50%; width: 104px; height: 104px;
    margin-left: -52px; border-radius: 50%;
  }
  .brand__name {
    position: absolute; left: 0; right: 0;
    font-size: 40px; font-weight: 600; line-height: 1; letter-spacing: 0.5px;
  }
  .brand__town {
    position: absolute; left: 0; right: 0;
    display: flex; align-items: center; justify-content: center; gap: 12px;
    font-size: 16px; font-weight: 400; letter-spacing: 2px; line-height: 1;
  }
  .brand__town::before, .brand__town::after {
    content: ""; width: 44px; height: 1.5px; background: currentColor;
  }

  .brand--front { left: 471px; top: 0; height: 508px; color: var(--paper); }
  .brand--front .brand__dot { top: 243px; background: var(--paper); }
  .brand--front .brand__name { top: 386px; }
  .brand--front .brand__town { top: 437px; }

  .brand--back { left: 469px; top: 0; height: 508px; color: var(--ink); }
  .brand--back .brand__dot { top: 247px; background: var(--ink); }
  .brand--back .brand__name { top: 378px; }
  .brand--back .brand__town { top: 434px; }

  .band { position: absolute; left: 0; top: 342px; width: 835px; height: 52px; }

  .contact {
    position: absolute; right: 62px; top: 70px;
    list-style: none; color: var(--ink);
  }
  .contact__row {
    display: flex; align-items: center; justify-content: flex-end;
    gap: 14px; height: 35px;
    font-size: 20.5px; font-weight: 400;
  }
  .contact__icon { width: 28px; height: 28px; flex: none; }
</style>
</head>
<body>
<main class="canvas">

  <section class="card card--front" aria-label="Vorderseite">
    <div class="front-pattern" role="img" aria-label="Dunkles Hintergrundmuster aus wiederholten Blütenmotiven"></div>
    <div class="brand brand--front">
      <div class="brand__dot"></div>
      <div class="brand__name">zum Anker</div>
      <div class="brand__town">Seestadt</div>
    </div>
  </section>

  <section class="card card--back" aria-label="Rückseite">
    <ul class="contact">
      <li class="contact__row">
        <span>Hafengasse 12, 78345 Seestadt</span>
        <svg class="contact__icon" viewBox="0 0 28 28" aria-hidden="true">
          <circle cx="14" cy="14" r="12.5" fill="none" stroke="#111" stroke-width="1.5"/>
          <path d="M14 6.5a5 5 0 0 0-5 5c0 3.8 5 9.5 5 9.5s5-5.7 5-9.5a5 5 0 0 0-5-5z" fill="#111"/>
          <circle cx="14" cy="11.5" r="1.9" fill="#fff"/>
        </svg>
      </li>
      <li class="contact__row">
        <span>07 623 420 186</span>
        <svg class="contact__icon" viewBox="0 0 28 28" aria-hidden="true">
          <circle cx="14" cy="14" r="12.5" fill="none" stroke="#111" stroke-width="1.5"/>
          <path d="M9.5 8.5l2.3-.5 1.3 3-1.5 1.2c.8 1.7 2 2.9 3.7 3.7l1.2-1.5 3 1.3-.5 2.3c-5.3.3-9.8-4.2-9.5-9.5z" fill="none" stroke="#111" stroke-width="1.3" stroke-linejoin="round"/>
        </svg>
      </li>
      <li class="contact__row">
        <span>info@zum-anker-seestadt.de</span>
        <svg class="contact__icon" viewBox="0 0 28 28" aria-hidden="true">
          <circle cx="14" cy="14" r="12.5" fill="none" stroke="#111" stroke-width="1.5"/>
          <rect x="8" y="10" width="12" height="8.5" fill="#111"/>
          <path d="M8 10l6 5 6-5" fill="none" stroke="#fff" stroke-width="1.2"/>
        </svg>
      </li>
      <li class="contact__row">
        <span>www.zum-anker-seestadt.de</span>
        <svg class="contact__icon" viewBox="0 0 28 28" aria-hidden="true">
          <circle cx="14" cy="14" r="12.5" fill="none" stroke="#111" stroke-width="1.5"/>
          <g fill="none" stroke="#111" stroke-width="1.2">
            <circle cx="14" cy="14" r="6.5"/>
            <ellipse cx="14" cy="14" rx="2.8" ry="6.5"/>
            <path d="M7.5 14h13M8.5 10.8h11M8.5 17.2h11"/>
          </g>
        </svg>
      </li>
    </ul>

    <svg class="band" viewBox="0 0 835 52" aria-hidden="true">
      <polygon points="0,0 487,0 409,52 0,52" fill="var(--band)"/>
      <polygon points="835,0 835,52 771,52" fill="var(--band-light)"/>
    </svg>

    <div class="brand brand--back">
      <div class="brand__dot"></div>
      <div class="brand__name">zum Anker</div>
      <div class="brand__town">Seestadt</div>
    </div>
  </section>

</main>
</body>
</html>
```